Web Design Project for Communications Agency

The design I need (PSD file) is for an agency offering specialised PR and communications services for customers in the healthcare sector.

OBJECTIVES OF THE WEBSITE:
1. To promote the agency's communication services
2. To position Pellerin Dautry as an industry leader, an expert in healthcare PR and communications by highlighting blogposts and social media.

WHAT I NEED:
1st, I need the design for the Home Page ONLY.
Once approved, I will need the other pages designed as well. (Here is prototype that we've already developed for the Website that will guide you in the design:
http://velocraft.example/pellerindautry/)

VISUAL INSPIRATION
We want to give this Website a "Flat Design" look. Here are some websites for inspiration :
- http://marbleforge.example/#!/process
- http://www.brisklane.example/
- http://tovalinework.example/

Also, reuse images found on the company's current Website :
http://www.pellerindautry.example/fr/index.html

HOMEPAGE MAIN ELEMENTS:
1. Main menu : 6 sections
Accueil | Agence | Services | Approche | Publications | Contact

2. Main Call To Action (big dark rectangle in prototype):
Can be slider or just an information bloc.

3. Publications récentes :
The 4 latest blog posts must be features on the homepage (will be linked with the "Publications" section)

4. Dynamic Footer :
Contains a Gazouillis feed and a Subscribe to our Newsletter feature (revecez nos publications)

OTHER PAGES (to design once Homepage is approved)
- Agence (about us)
- Services (our team)
- Approche (our approach)
- Publications (blog articles)
- Contact (Contact us)

• Please refer to prototype :
http://velocraft.example/pellerindautry/
Must have ALL features present in prototype.

Also, must reuse this picture in the design : http://pellerindautry.example/static/images/home-big-box.jpg

Finally, you will find attached the company logo.

```html
<!DOCTYPE html>
<html lang="fr">
<head>
<meta charset="utf-8">
<title>Pellerin Dautry – Gestion d'enjeux, affaires publiques</title>
<link rel="stylesheet" href="https://fonts.googleapis.com/css2?family=Arvo:wght@400;700&family=Arimo:wght@400;700&family=Cabin:wght@400;500&family=Ubuntu:wght@500&display=swap">
<style>
  :root{
    --header-bg:#464646;
    --brand-red:#e14b4f;
    --nav-red:#e0484c;
    --cta-red:#cc2d3d;
    --title-red:#e4504f;
    --ink:#3f3f3f;
    --muted:#c4b8bd;
    --footer-bg:#2d2d2d;
    --footer-text:#b9b9b9;
    --field-bg:#4a4a4a;
    --join:#f5575b;
    --bottom-bg:#242424;
    --tweet-link:#e84b4f;
    --sky:#3bbfea;
  }
  *{margin:0;padding:0;box-sizing:border-box}
  html,body{width:1200px;height:2169px;overflow:hidden;background:#fff}
  body{position:relative;font-family:'Cabin',sans-serif;color:var(--ink)}

  .site-header{position:absolute;left:0;top:0;width:1200px;height:108px;background:var(--header-bg)}
  .brand{position:absolute;left:492px;top:26px;display:flex;align-items:center;gap:14px}
  .brand-name{font-family:'Cabin',sans-serif;font-size:30px;line-height:28px;color:var(--brand-red);width:110px}
  .brand-tag{font-family:'Ubuntu',sans-serif;font-weight:500;font-size:11px;line-height:14px;color:#fff;border-left:2px solid var(--brand-red);padding-left:8px}

  .main-nav{position:absolute;left:0;top:108px;width:1200px;height:52px;background:var(--nav-red)}
  .main-nav a{position:absolute;top:16px;font-family:'Ubuntu',sans-serif;font-weight:500;font-size:15px;color:#fff;text-decoration:none;transform:translateX(-50%)}
  .social{position:absolute;top:16px;left:918px;display:flex;gap:22px}
  .social span{width:20px;height:20px;border:2px solid #fff;border-radius:50%}

  .hero{position:absolute;left:0;top:160px;width:1200px;height:583px;
    background:linear-gradient(90deg,#6d5848 0%,#b9a48e 18%,#d9dbe2 40%,#cfd4e0 60%,#a59a8a 82%,#7f6a58 100%)}
  .hero-floor{position:absolute;left:0;bottom:0;width:100%;height:250px;background:linear-gradient(180deg,rgba(120,130,170,0) 0%,rgba(90,105,160,.45) 100%)}
  .hero-panel{position:absolute;left:111px;top:67px;width:979px;height:217px;background:rgba(240,240,242,.86);text-align:center}
  .hero-panel h1{font-family:'Arvo',serif;font-weight:400;font-size:31px;line-height:40px;color:#4a4a4a;margin-top:40px}
  .hero-cta{display:inline-block;margin-top:23px;width:184px;height:38px;line-height:38px;background:var(--cta-red);color:#fff;font-family:'Arvo',serif;font-weight:700;font-size:18px;text-decoration:none}
  .hero-cube{position:absolute;left:481px;top:300px;width:242px;height:234px;background:radial-gradient(circle at 50% 30%,#d23642 0%,#c92a38 28%,#f3f3f3 32%,#d9d9d9 80%,rgba(217,217,217,0) 100%)}

  .recent{position:absolute;left:116px;top:786px;width:968px}
  .recent h2{font-family:'Arimo',sans-serif;font-weight:400;font-size:49px;color:#444;letter-spacing:.5px}

  .post{position:absolute;width:464px}
  .post h3{font-family:'Cabin',sans-serif;font-weight:400;font-size:19px;color:var(--title-red);height:34px;border-bottom:2px dotted #e2e2e2}
  .post-photo{display:block;margin-top:28px;width:462px;height:185px}
  .post p{margin-top:20px;font-size:13.5px;line-height:22px;color:var(--muted);width:458px}
  .view-all{display:inline-block;margin-top:16px;margin-left:3px;width:98px;height:25px;line-height:25px;text-align:center;border-radius:3px;background:linear-gradient(180deg,#4a4a4a 0%,#0d0d0d 100%);color:#fff;font-family:'Arimo',sans-serif;font-weight:700;font-size:13px;text-decoration:none}
  .photo-warm{background:linear-gradient(120deg,#e9e4df 0%,#c7a893 45%,#f2efec 100%)}
  .photo-ward{background:linear-gradient(120deg,#d9cdbd 0%,#3a62b0 45%,#e7e2dc 100%)}
  .photo-nursery{background:linear-gradient(120deg,#9aa0ac 0%,#dcdde3 50%,#8f95a3 100%)}
  .photo-team{background:linear-gradient(120deg,#d8c7b4 0%,#f1ede8 50%,#c8b39f 100%)}

  .site-footer{position:absolute;left:0;top:1774px;width:1200px;height:331px;background:var(--footer-bg)}
  .feed-name{position:absolute;left:124px;top:30px;font-family:'Cabin',sans-serif;font-weight:500;font-size:56px;line-height:64px;color:var(--sky)}
  .tweets{position:absolute;left:125px;top:125px;width:440px}
  .tweets p{font-family:'Arimo',sans-serif;font-size:13px;line-height:17px;color:var(--footer-text);margin-bottom:18px}
  .tweets a{color:var(--tweet-link);text-decoration:none}
  .newsletter{position:absolute;left:645px;top:70px;width:435px}
  .newsletter h4{font-family:'Arimo',sans-serif;font-weight:400;font-size:18px;color:#fff;margin-left:3px}
  .field{display:block;width:435px;height:52px;margin-top:26px;background:var(--field-bg);border:0;padding-left:16px;font-family:'Cabin',sans-serif;font-size:14px;color:#9a9a9a;line-height:52px}
  .field+.field{margin-top:26px}
  .join{display:block;margin-top:26px;width:131px;height:34px;line-height:34px;text-align:center;background:var(--join);border-radius:2px;color:#fff;font-family:'Cabin',sans-serif;font-size:14px;text-decoration:none}

  .bottom-bar{position:absolute;left:0;top:2105px;width:1200px;height:64px;background:var(--bottom-bg);text-align:center;line-height:64px;font-family:'Cabin',sans-serif;font-size:12px;color:#9d9d9d}
  .bottom-bar strong{color:#fff;font-weight:400}
</style>
</head>
<body>

<header class="site-header">
  <div class="brand">
    <span class="brand-name">Pellerin Dautry</span>
    <span class="brand-tag">GESTION D'ENJEUX<br>AFFAIRES PUBLIQUES</span>
  </div>
</header>

<nav class="main-nav">
  <a href="#" style="left:155px">Accueil</a>
  <a href="#" style="left:265px">Agence</a>
  <a href="#" style="left:379px">Services</a>
  <a href="#" style="left:502px">Approche</a>
  <a href="#" style="left:638px">Publications</a>
  <a href="#" style="left:768px">Contact</a>
  <div class="social"><span></span><span></span><span></span><span></span></div>
</nav>

<section class="hero" role="img" aria-label="Couloir d'hôpital flou en arrière-plan">
  <div class="hero-floor"></div>
  <div class="hero-panel">
    <h1>Cabinet-conseil en communications et affaires publiques<br>spécialisé dans le secteur de la santé.</h1>
    <a class="hero-cta" href="#">En Savior Plus</a>
  </div>
  <div class="hero-cube" role="img" aria-label="Cube blanc portant une croix rouge"></div>
</section>

<section class="recent">
  <h2>Publication Récentes</h2>
</section>

<article class="post" style="left:116px;top:880px">
  <h3>Titre de la publication</h3>
  <div class="post-photo photo-warm" role="img" aria-label="Infirmière souriante avec une patiente âgée"></div>
  <p>Lorem Ipsum est simplement du faux texte employé dans la sition et la misen page avant impression. Le Lorem Ipsum est le faux texte standard de l'imprimerie depuis les années 1500.</p>
  <a class="view-all" href="#">View All</a>
</article>

<article class="post" style="left:617px;top:880px">
  <h3>Titre de la publication</h3>
  <div class="post-photo photo-ward" role="img" aria-label="Infirmière consultant un dossier près d'un patient alité" style="margin-left:5px"></div>
  <p>Lorem Ipsum est simplement du faux texte employé dans la sition et la misen page avant impression. Le Lorem Ipsum est le faux texte standard de l'imprimerie depuis les années 1500.</p>
  <a class="view-all" href="#">View All</a>
</article>

<article class="post" style="left:116px;top:1292px">
  <h3>Titre de la publication</h3>
  <div class="post-photo photo-nursery" role="img" aria-label="Nouveau-nés dans des berceaux de pouponnière"></div>
  <p>Lorem Ipsum est simplement du faux texte employé dans la sition et la misen page avant impression. Le Lorem Ipsum est le faux texte standard de l'imprimerie depuis les années 1500, quand un peintre anonyme assembla ensemble des morceaux de texte pour réaliser un livre spécimen de olices de texte.</p>
  <a class="view-all" href="#">View All</a>
</article>

<article class="post" style="left:617px;top:1292px">
  <h3>Titre de la publication</h3>
  <div class="post-photo photo-team" role="img" aria-label="Équipe de professionnels de la santé" style="margin-left:5px"></div>
  <p>Lorem Ipsum est simplement du faux texte employé dans la sition et la misen page avant impression. Le Lorem Ipsum est le faux texte standard de l'imprimerie depuis les années 1500, quand un peintre anonyme assembla ensemble des morceaux de texte pour réaliser un livre spécimen de olices de texte.</p>
  <a class="view-all" href="#">View All</a>
</article>

<footer class="site-footer">
  <div class="feed-name">Gazouillis</div>
  <div class="tweets">
    <p>Dolore eu feugiat nulla facilisis at vero eros et accumsan et iusto odio dignissim qui blandit praesent <a href="#">@luptatum zzril delenit augue duis dolore</a></p>
    <p>Dolore eu feugiat nulla facilisis at vero eros et accumsan et iusto odio dignissim qui blandit praesent <a href="#">@luptatum zzril delenit augue duis dolore</a></p>
    <p>Dolore eu feugiat nulla facilisis at vero eros et accumsan et iusto odio dignissim qui blandit praesent <a href="#">@luptatum zzril delenit augue duis dolore</a></p>
  </div>
  <form class="newsletter">
    <h4>Recevez nos publications</h4>
    <div class="field">Votre nom</div>
    <div class="field">Votre courriel</div>
    <a class="join" href="#">Join Us Now</a>
  </form>
</footer>

<div class="bottom-bar">© 2013 <strong>Pellerin Dautry</strong> All rights reserved.</div>

</body>
</html>
```